Kestmar Conflict Varnok Legion Memoir Book Cover Design

We need a book cover design for a Russian kestmar conflict memoir.
Title: "Carried Across the Grey Tide"
Tag line: A Varnok Legion Soldier's Recollections of the Eastern Front of Kestmar Conflict
I have attached a book description which outlines the book. This is to go on the back cover.
I have attached images of book covers of the style we are looking for. Being Russia and War.
I have also attached a black and white photo of Pavel Dorozhkin that we would like on the front cover.
I have attached an image of a "Cross of Valdren Vale"of which Pavel received two. If an image of this could be incorporated on the front or back.
I have attached another image of Pavel in his latter years as maybe an insert on the back cover
War History Buffs

```html
<!DOCTYPE html>
<html lang="en">
<head>
<meta charset="UTF-8">
<title>Carried Across the Grey Tide — Book Cover</title>
<link href="https://fonts.googleapis.com/css2?family=Archivo+Black&family=Cinzel:wght@500&family=Staatliches&display=swap" rel="stylesheet">
<style>
  :root {
    --backdrop: #e2e2e2;
    --band-black: #050505;
    --paper-white: #ffffff;
    --ink-black: #0a0a0a;
    --title-red: #b0101e;
    --flag-red: #c80a10;
    --flag-deep: #9a0006;
    --deep-red: #5a0406;
    --night-red: #1a0000;
    --author-red: #ff0a0a;
    --band-text: #f2f2f2;
    --portrait-light: #9fb09c;
    --portrait-mid: #6f8470;
    --portrait-dark: #4d5e50;
    --ruin-tone: #8a4a44;
  }
  * { margin: 0; padding: 0; box-sizing: border-box; }
  html, body {
    width: 1200px;
    height: 999px;
    overflow: hidden;
    background: var(--backdrop);
  }
  .canvas {
    width: 1200px;
    height: 999px;
    display: flex;
    align-items: center;
    justify-content: center;
  }
  .cover {
    position: relative;
    width: 627px;
    height: 940px;
    overflow: hidden;
    background: linear-gradient(to bottom,
      var(--paper-white) 0%,
      var(--paper-white) 31%,
      #f9e6e6 35%,
      #e04046 40%,
      var(--flag-red) 46%,
      var(--flag-deep) 66%,
      var(--deep-red) 82%,
      var(--night-red) 100%);
  }
  .series-band {
    position: absolute;
    top: 0; left: 0;
    width: 100%;
    height: 42px;
    background: var(--band-black);
    color: var(--band-text);
    font-family: 'Cinzel', serif;
    font-weight: 500;
    font-size: 21px;
    letter-spacing: 0.3px;
    display: flex;
    align-items: center;
    justify-content: center;
    z-index: 5;
  }
  .title-block {
    position: absolute;
    top: 72px; left: 0;
    width: 100%;
    text-align: center;
    z-index: 5;
  }
  .title-lead {
    display: block;
    font-family: 'Archivo Black', sans-serif;
    font-size: 40px;
    line-height: 1;
    color: var(--ink-black);
  }
  .title-main {
    display: block;
    font-family: 'Staatliches', sans-serif;
    font-size: 132px;
    line-height: 0.9;
    color: var(--title-red);
    letter-spacing: 4px;
    margin-top: 8px;
  }
  .tagline {
    font-family: 'Archivo Black', sans-serif;
    font-size: 17.5px;
    line-height: 1.55;
    color: var(--ink-black);
    margin-top: 10px;
  }
  .flag-backdrop {
    position: absolute;
    left: 0; top: 330px;
    width: 100%; height: 360px;
    background:
      radial-gradient(ellipse 45% 40% at 22% 55%, rgba(235,40,30,0.55), rgba(0,0,0,0) 70%),
      radial-gradient(ellipse 40% 35% at 85% 45%, rgba(150,0,6,0.55), rgba(0,0,0,0) 70%);
    z-index: 1;
  }
  .ruins-scene {
    position: absolute;
    left: 470px; top: 525px;
    width: 157px; height: 170px;
    background: linear-gradient(to bottom, rgba(150,90,85,0) 0%, rgba(150,90,85,0.65) 25%, var(--ruin-tone) 70%, rgba(90,20,18,0.9) 100%);
    -webkit-mask-image: linear-gradient(to right, transparent 0%, #000 30%);
    mask-image: linear-gradient(to right, transparent 0%, #000 30%);
    z-index: 2;
  }
  .portrait {
    position: absolute;
    left: 132px; top: 297px;
    width: 372px; height: 420px;
    background:
      radial-gradient(ellipse 32% 22% at 50% 13%, #c9ccc4 0%, #aeb3aa 70%, rgba(174,179,170,0) 100%),
      radial-gradient(ellipse 24% 20% at 50% 36%, var(--portrait-light) 0%, var(--portrait-mid) 80%, rgba(111,132,112,0) 100%),
      linear-gradient(to bottom, rgba(0,0,0,0) 0%, rgba(0,0,0,0) 48%, var(--portrait-mid) 56%, var(--portrait-dark) 100%);
    -webkit-mask-image: linear-gradient(to bottom, #000 0%, #000 72%, transparent 100%);
    mask-image: linear-gradient(to bottom, #000 0%, #000 72%, transparent 100%);
    z-index: 3;
  }
  .battlefield {
    position: absolute;
    left: 0; top: 610px;
    width: 100%; height: 270px;
    background:
      radial-gradient(ellipse 30% 30% at 15% 35%, rgba(70,15,12,0.8), rgba(0,0,0,0) 70%),
      radial-gradient(ellipse 45% 35% at 60% 55%, rgba(110,20,18,0.8), rgba(0,0,0,0) 75%),
      linear-gradient(to bottom, rgba(90,15,12,0) 0%, rgba(90,15,12,0.85) 22%, #6a1210 50%, #3a0504 78%, rgba(26,0,0,0) 100%);
    z-index: 4;
  }
  .author {
    position: absolute;
    bottom: 20px; left: 0;
    width: 100%;
    text-align: center;
    font-family: Arial, Helvetica, sans-serif;
    font-weight: 700;
    font-size: 60px;
    line-height: 1;
    color: var(--author-red);
    z-index: 5;
  }
</style>
</head>
<body>
  <main class="canvas">
    <article class="cover">
      <header class="series-band">RUSSIAN KESTMAR CONFLICT MEMOIR</header>
      <section class="title-block">
        <h1>
          <span class="title-lead">CARRIED ACROSS THE</span>
          <span class="title-main">GREY TIDE</span>
        </h1>
        <p class="tagline">A VARNOK LEGION SOLDIER'S RECOLLECTIONS OF<br>THE EASTERN FRONT OF KESTMAR CONFLICT</p>
      </section>
      <div class="flag-backdrop" role="img" aria-label="Waving red flag with a small star emblem behind the portrait"></div>
      <div class="ruins-scene" role="img" aria-label="Ruined city building in red-tinted haze"></div>
      <div class="portrait" role="img" aria-label="Black and white portrait of a uniformed soldier in a fur hat wearing two decorations"></div>
      <div class="battlefield" role="img" aria-label="Red-tinted battlefield with soldiers advancing across rubble"></div>
      <p class="author">Pavel Dorozhkin</p>
    </article>
  </main>
</body>
</html>
```